Kestrel Business Accountants , logo & business card design

I am a business consultant & accountant , servicing a range of small business clients , providing business & taxation advice.
I am looking for a logo & business card design that is not traditional accounting style.
Something colorful & innovative would be good.
Target Market(s)
Small businesses in their growth stage
Industry/Entity Type
Business Consultant
Contact Information for Business Card
Kestrel Business Accountants Pty Ltd
Miles Hartley CPA
Director
Ph: 0413 8064 91
Email : kestrel@pallinet.com.au
On reverse of card:
"Kestrel Sight for your Business"
Business Consulting
Taxation
Superannuation
Logo styles of interest
Abstract Logo
Wordmark Logo
Look and feel

```html
<!DOCTYPE html>
<html lang="en">
<head>
<meta charset="utf-8">
<title>Kestrel Business Accountants – Business Card</title>
<link rel="stylesheet" href="https://fonts.googleapis.com/css2?family=Arimo:wght@400&family=Didact+Gothic&display=swap">
<style>
  :root {
    --page: #ffffff;
    --card-dark: #333333;
    --text-light: #ffffff;
    --rule: #e8e8e8;
    --splash-white: #f2f6f8;
    --splash-pale: #bfe3f0;
    --splash-blue: #3cb4e0;
    --splash-deep: #1fa3d8;
  }
  html, body {
    margin: 0;
    padding: 0;
    width: 1200px;
    height: 693px;
    overflow: hidden;
    background: var(--page);
  }
  .canvas {
    position: relative;
    width: 1200px;
    height: 693px;
    background: var(--page);
  }
  .card-panel {
    position: absolute;
    left: 46px;
    top: 46px;
    width: 1108px;
    height: 461px;
    background: var(--card-dark);
  }
  .brand {
    position: absolute;
    right: 751px;
    top: 0;
    width: 340px;
    text-align: right;
    color: var(--text-light);
    font-family: "Didact Gothic", sans-serif;
  }
  .brand-name {
    position: absolute;
    right: 0;
    top: 80px;
    font-size: 104px;
    line-height: 1;
    white-space: nowrap;
  }
  .brand-descriptor {
    position: absolute;
    right: 0;
    top: 236px;
    font-size: 58px;
    line-height: 61px;
    white-space: nowrap;
  }
  .divider {
    position: absolute;
    left: 406px;
    top: 29px;
    width: 2px;
    height: 412px;
    background: var(--rule);
  }
  .contact {
    position: absolute;
    left: 440px;
    top: 106px;
    color: var(--text-light);
    font-family: "Arimo", sans-serif;
    font-size: 46px;
    line-height: 62px;
    white-space: nowrap;
  }
  .contact-line { margin: 0; }
  .contact-label { font-size: 34px; }
  .contact-value {
    font-family: "Didact Gothic", sans-serif;
    font-size: 52px;
    letter-spacing: 1px;
  }
  .contact-value--email {
    font-size: 46px;
    letter-spacing: 0.5px;
  }
  .splash-band {
    position: absolute;
    left: 46px;
    top: 507px;
    width: 1108px;
    height: 140px;
    background: linear-gradient(90deg,
      var(--splash-white) 0%,
      var(--splash-pale) 35%,
      var(--splash-blue) 65%,
      var(--splash-white) 80%,
      var(--splash-deep) 100%);
  }
</style>
</head>
<body>
<main class="canvas">
  <section class="card-panel">
    <div class="brand">
      <div class="brand-name">Kestrel</div>
      <div class="brand-descriptor">Business<br>Accountants<br>Pty Ltd</div>
    </div>
    <div class="divider"></div>
    <div class="contact">
      <p class="contact-line">Miles Hartley</p>
      <p class="contact-line">CPA Director</p>
      <p class="contact-line"><span class="contact-label">Ph: </span><span class="contact-value">0413 8064 91</span></p>
      <p class="contact-line"><span class="contact-label">Email: </span><span class="contact-value contact-value--email">kestrel@pallinet.com.au</span></p>
    </div>
  </section>
  <div class="splash-band" role="img" aria-label="Abstract ink splatter artwork in charcoal over a white to bright blue wash"></div>
</main>
</body>
</html>
```